KORBALT

The business want a professional looking business card. We have a scetch we will add but want the extra upgrade, and would like more suggestions for variations of our business cards.

```html
<!DOCTYPE html>
<html lang="en">
<head>
<meta charset="UTF-8">
<title>KORBALT – Business Card</title>
<link href="https://fonts.googleapis.com/css2?family=Cinzel:wght@500;600&family=Montserrat:wght@400;500&display=swap" rel="stylesheet">
<style>
  :root {
    --bg-light: #e9e9e7;
    --bg-dark: #cfcfcc;
    --brown-dark: #3a2108;
    --brown-mid: #4f300f;
    --brown-edge: #6b4514;
    --gold: #c9a24a;
    --gold-light: #e6cd8a;
    --gold-pale: #efe3bd;
    --gold-deep: #8a6a22;
    --ink-gold: #6e5216;
    --white: #f4efe4;
  }
  * { margin: 0; padding: 0; box-sizing: border-box; }
  html, body { width: 1200px; height: 801px; overflow: hidden; }
  body {
    background: radial-gradient(ellipse at 50% 40%, var(--bg-light) 0%, var(--bg-dark) 100%);
    position: relative;
    font-family: 'Montserrat', sans-serif;
  }
  .card {
    position: absolute;
    top: 246px;
    width: 540px;
    height: 309px;
    border-radius: 3px;
    box-shadow: 0 14px 30px rgba(0,0,0,0.22), 0 2px 4px rgba(0,0,0,0.15);
    overflow: hidden;
  }

  /* Front: brown contact card */
  .card-front {
    left: 40px;
    background: linear-gradient(135deg, var(--brown-mid) 0%, var(--brown-dark) 100%);
    border: 2px solid var(--brown-edge);
  }
  .brand-block {
    position: absolute;
    left: 40px;
    top: 96px;
    width: 190px;
    text-align: center;
  }
  .brand-dot {
    width: 38px; height: 38px;
    border-radius: 50%;
    background: var(--gold);
    margin: 0 auto 14px;
  }
  .brand-name {
    font-family: 'Cinzel', serif;
    font-weight: 600;
    font-size: 24px;
    letter-spacing: 4px;
    color: var(--gold);
  }
  .brand-since {
    font-family: 'Montserrat', sans-serif;
    font-size: 8px;
    letter-spacing: 3px;
    color: var(--gold);
    margin-top: 2px;
  }
  .divider {
    position: absolute;
    left: 262px;
    top: 56px;
    width: 1px;
    height: 196px;
    background: var(--gold);
    opacity: 0.8;
  }
  .contact-block {
    position: absolute;
    left: 286px;
    top: 62px;
    width: 240px;
  }
  .person-name {
    font-family: 'Cinzel', serif;
    font-weight: 600;
    font-size: 17px;
    letter-spacing: 1px;
    color: var(--gold-light);
  }
  .person-role {
    font-size: 14px;
    color: var(--white);
    margin-top: 4px;
  }
  .person-full {
    font-size: 8px;
    color: var(--white);
    opacity: 0.75;
    margin-top: 3px;
  }
  .contact-list {
    list-style: none;
    margin-top: 30px;
  }
  .contact-list li {
    display: flex;
    align-items: center;
    gap: 8px;
    font-size: 11px;
    color: var(--white);
    margin-bottom: 8px;
  }
  .contact-icon {
    width: 12px; height: 12px;
    flex: none;
  }

  /* Back: gold brand card */
  .card-back {
    left: 620px;
    background: linear-gradient(115deg, var(--gold-pale) 0%, var(--gold) 45%, var(--gold-deep) 100%);
    border: 2px solid var(--brown-edge);
  }
  .back-brand {
    position: absolute;
    left: 0; right: 0;
    top: 112px;
    text-align: center;
  }
  .back-name {
    font-family: 'Cinzel', serif;
    font-weight: 500;
    font-size: 50px;
    letter-spacing: 12px;
    color: var(--ink-gold);
  }
  .back-since {
    font-family: 'Montserrat', sans-serif;
    font-size: 13px;
    letter-spacing: 6px;
    color: var(--ink-gold);
    margin-top: 2px;
  }
</style>
</head>
<body>

  <section class="card card-front">
    <div class="brand-block">
      <div class="brand-dot"></div>
      <div class="brand-name">KORBALT</div>
      <div class="brand-since">SINCE 2026</div>
    </div>

    <div class="divider"></div>

    <div class="contact-block">
      <div class="person-name">KORBALT VARDEN</div>
      <div class="person-role">CEO &amp; Founder</div>
      <div class="person-full">Aksel Varden Moen</div>

      <ul class="contact-list">
        <li>
          <svg class="contact-icon" viewBox="0 0 12 12"><circle cx="6" cy="6" r="6" fill="#c9a24a"/><path d="M4 3.2 L5 3.2 L5.4 4.6 L4.8 5.1 Q5.5 6.6 6.9 7.2 L7.4 6.6 L8.8 7 L8.8 8 Q8.6 8.8 7.6 8.7 Q4.2 8.2 3.3 4.4 Q3.3 3.4 4 3.2 Z" fill="#3a2108"/></svg>
          004791234567
        </li>
        <li>
          <svg class="contact-icon" viewBox="0 0 12 12"><circle cx="6" cy="6" r="6" fill="#c9a24a"/><rect x="3" y="4" width="6" height="4.2" fill="none" stroke="#3a2108" stroke-width="0.9"/><path d="M3 4 L6 6.3 L9 4" fill="none" stroke="#3a2108" stroke-width="0.9"/></svg>
          korbalt.llc@postmail.com
        </li>
        <li>
          <svg class="contact-icon" viewBox="0 0 12 12"><circle cx="6" cy="6" r="6" fill="#c9a24a"/><circle cx="6" cy="6" r="3.2" fill="none" stroke="#3a2108" stroke-width="0.8"/><ellipse cx="6" cy="6" rx="1.4" ry="3.2" fill="none" stroke="#3a2108" stroke-width="0.7"/><line x1="2.8" y1="6" x2="9.2" y2="6" stroke="#3a2108" stroke-width="0.7"/></svg>
          www.korbalt.llc
        </li>
      </ul>
    </div>
  </section>

  <section class="card card-back">
    <div class="back-brand">
      <div class="back-name">KORBALT</div>
      <div class="back-since">SINCE 2026</div>
    </div>
  </section>

</body>
</html>
```